Hair Extension Packaging

Update 2/16 - please keep submissions coming, I have no front runners yet. Thanks.

I need some new packaging designed for hair extensions. I have enclose pictures of what other companies packaging looks like and a few pictures of some inspiration. I am looking for a packaging that will appeal to a 20's-30's year old demographic and I like things along the lines of glamor/lace/vintage/boudoir/damask inspired. I am going to leave colors up to your creativity for the sample artwork and ask for changes if needed. Id like the design to be a standout but not loud.

The working name for this hair is "Vexa"
Additional Text that I would like on the packaging "100% Premium Virgin Remy Human Hair"

Please keep in mind that the background of the packaging will have many different colors laying over it so be mindful of what the color you chose can effect the hair color in the packaging - no red or orange which can make the hair appear very warm and clash with ashy colors.

Working dimensions for the sample are 22" long, 3" wide.

****Once I decide on the front of the packaging I will also need the back designed which will consist of similar design as the front but with hair care instructions printed on it.***** This finished product must include front and back artwork, open Photoshop files, and additional bleed room for printing. I don't want to waste anyone's time so once I get a front design I like I will work with that artist to create the back.

Please message me with any questions.
Updates

Project Deadline Extended
Reason: Finalizing final choices. Thanks for your submissions!

Target Market(s)

Women in there 20"s - 30's. High fashion, luxurious, glamour

Industry/Entity Type

Hair

Font styles to use
Serif
Script

Requirements
Must have
• Id love the product name to be in script and then mixed with regular font (see the makeup logo example I enclosed)
Should not have
• Should not be masculine. Forget the blue and green colors

```html
<!DOCTYPE html>
<html lang="en">
<head>
<meta charset="utf-8">
<title>Vexa Hair Extension Packaging</title>
<link rel="stylesheet" href="https://fonts.googleapis.com/css2?family=Great+Vibes&family=Mulish:wght@400;600&display=swap">
<style>
  :root {
    --backdrop: #8a817a;
    --panel: #fbfaf8;
    --panel-tint: #f4f1ed;
    --frame-line: #eee3d6;
    --body-ink: #8d8782;
    --onyx: #151515;
    --taupe: #cbc1b5;
    --cream: #eae0d0;
    --blonde-1: #e6d8cb;
    --blonde-2: #b9a597;
    --brunette-1: #2c1a10;
    --brunette-2: #8b6a53;
  }
  * { margin: 0; padding: 0; box-sizing: border-box; }
  html, body { width: 1200px; height: 2604px; overflow: hidden; }
  body {
    background: var(--backdrop);
    position: relative;
    font-family: "Mulish", Arial, sans-serif;
  }
  .package {
    position: absolute;
    top: 271px;
    width: 298px;
    height: 2062px;
    background: linear-gradient(180deg, var(--panel) 0%, var(--panel-tint) 100%);
    box-shadow: 0 8px 22px rgba(0,0,0,.35);
    overflow: hidden;
  }
  .package--onyx { left: 65px; --accent: var(--onyx); --hair-a: #050505; --hair-b: #4a4a4a; --label-bg: #fbfaf8; --label-ink: #151515; --badge-bg: #111; --badge-ink: #fff; --badge-ring: #111; --frame: var(--frame-line); --script-ink: #fff; }
  .package--blonde { left: 451px; --accent: var(--taupe); --hair-a: var(--blonde-1); --hair-b: var(--blonde-2); --label-bg: #fbfaf8; --label-ink: #b8ada1; --badge-bg: #fbfaf8; --badge-ink: #222; --badge-ring: #111; --frame: #cfc6bb; --script-ink: #2a2522; }
  .package--brunette { left: 840px; --accent: var(--cream); --hair-a: var(--brunette-1); --hair-b: var(--brunette-2); --label-bg: #b7aea6; --label-ink: #fff; --badge-bg: #c9c1b8; --badge-ink: #222; --badge-ring: #fbfaf8; --frame: var(--frame-line); --script-ink: #fff; }

  .package__shapes { position: absolute; inset: 0; width: 298px; height: 2062px; }
  .hair-swatch-a { stop-color: var(--hair-a); }
  .hair-swatch-b { stop-color: var(--hair-b); }
  .base-band { fill: var(--accent); }

  .brand-name {
    position: absolute;
    top: 62px; left: 0; width: 100%;
    text-align: center;
    font-family: "Great Vibes", cursive;
    font-size: 96px;
    line-height: 1;
    color: var(--script-ink);
  }

  .quality-badge {
    position: absolute;
    left: 17px; top: 245px;
    width: 108px; height: 108px;
    border-radius: 50%;
    background: var(--badge-bg);
    border: 4px solid var(--badge-ring);
    color: var(--badge-ink);
    display: flex; flex-direction: column; align-items: center; justify-content: center;
    text-align: center;
    font-size: 12px; font-weight: 600; line-height: 1.25;
  }
  .quality-badge strong { font-size: 16px; }

  .story-frame {
    position: absolute;
    left: 70px; top: 716px;
    width: 158px; height: 738px;
    border: 5px solid var(--frame);
    background: var(--panel);
    display: flex; align-items: center; justify-content: center;
  }
  .story-text {
    writing-mode: vertical-rl;
    transform: rotate(180deg);
    font-size: 14px;
    line-height: 24px;
    color: var(--body-ink);
    height: 680px;
    text-align: justify;
  }

  .quality-label {
    position: absolute;
    right: 22px; top: 1948px;
    padding: 3px 10px;
    background: var(--label-bg);
    color: var(--label-ink);
    font-size: 13px; font-weight: 600; letter-spacing: .5px;
  }
  .quality-script {
    position: absolute;
    right: 44px; top: 1966px;
    font-family: "Great Vibes", cursive;
    font-size: 66px; line-height: 1;
    color: #fff;
  }
</style>
</head>
<body>

<section class="package package--onyx">
  <svg class="package__shapes" viewBox="0 0 298 2062" role="img" aria-label="Close-up photo of glossy jet black hair">
    <defs>
      <linearGradient id="hair-onyx" x1="0" y1="0" x2="1" y2="1">
        <stop offset="0" class="hair-swatch-b"/><stop offset="1" class="hair-swatch-a"/>
      </linearGradient>
    </defs>
    <polygon points="0,0 298,0 298,174 0,262" fill="url(#hair-onyx)"/>
    <polygon class="base-band" points="0,1964 298,1899 298,2062 0,2062"/>
  </svg>
  <div class="brand-name">Vexa</div>
  <div class="quality-badge"><strong>100%</strong>Premium<br>Virgin Remy<br>Human Hair</div>
  <div class="story-frame"><p class="story-text">Ondrelle Clip In Hair Extensions use only the finest quality Remy Human Hair, which means that the hair has been carefully sorted after collecting from the hair donor to ensure all the cuticles are of the same length. It is by far the best quality of Clip In Human Hair Extensions on the market because of the care that is required and the time it takes to sort the hair so meticulously.</p></div>
  <div class="quality-label">HIGH QUALITY</div>
  <div class="quality-script">hair</div>
</section>

<section class="package package--blonde">
  <svg class="package__shapes" viewBox="0 0 298 2062" role="img" aria-label="Close-up photo of soft ash blonde hair">
    <defs>
      <linearGradient id="hair-blonde" x1="0" y1="0" x2="1" y2="1">
        <stop offset="0" class="hair-swatch-b"/><stop offset="1" class="hair-swatch-a"/>
      </linearGradient>
    </defs>
    <polygon points="0,0 298,0 298,174 0,262" fill="url(#hair-blonde)"/>
    <line x1="0" y1="264" x2="298" y2="176" stroke="#111" stroke-width="6"/>
    <polygon class="base-band" points="0,1964 298,1899 298,2062 0,2062"/>
  </svg>
  <div class="brand-name">Vexa</div>
  <div class="quality-badge"><strong>100%</strong>Premium<br>Virgin Remy<br>Human Hair</div>
  <div class="story-frame"><p class="story-text">Ondrelle Clip In Hair Extensions use only the finest quality Remy Human Hair, which means that the hair has been carefully sorted after collecting from the hair donor to ensure all the cuticles are of the same length. It is by far the best quality of Clip In Human Hair Extensions on the market because of the care that is required and the time it takes to sort the hair so meticulously.</p></div>
  <div class="quality-label">HIGH QUALITY</div>
  <div class="quality-script">hair</div>
</section>

<section class="package package--brunette">
  <svg class="package__shapes" viewBox="0 0 298 2062" role="img" aria-label="Close-up photo of rich chestnut brown hair">
    <defs>
      <linearGradient id="hair-brunette" x1="0" y1="0" x2="1" y2="1">
        <stop offset="0" class="hair-swatch-a"/><stop offset="1" class="hair-swatch-b"/>
      </linearGradient>
    </defs>
    <polygon points="0,0 298,0 298,174 0,262" fill="url(#hair-brunette)"/>
    <polygon class="base-band" points="0,1964 298,1899 298,2062 0,2062"/>
  </svg>
  <div class="brand-name">Vexa</div>
  <div class="quality-badge"><strong>100%</strong>Premium<br>Virgin Remy<br>Human Hair</div>
  <div class="story-frame"><p class="story-text">Ondrelle Clip In Hair Extensions use only the finest quality Remy Human Hair, which means that the hair has been carefully sorted after collecting from the hair donor to ensure all the cuticles are of the same length. It is by far the best quality of Clip In Human Hair Extensions on the market because of the care that is required and the time it takes to sort the hair so meticulously.</p></div>
  <div class="quality-label">HIGH QUALITY</div>
  <div class="quality-script">hair</div>
</section>

</body>
</html>
```